I need a business card for a residential and apartment building development company. The card should be very high end prestige. Possibly a black card with a foil?? The card should be classical and simple yet very high end. The company currently does not have a logo so we can use graphical elements that suggest a building developement company.

Maverno Holdings LLC
917-555-2817 phone
877-555-4139 fax
Dalen.Okorafor@vintramail.com
General Construction Real Estate Investments and Development
47 Pelbrook Terrace
North 3D
Bronx, NY 10482

```html
<!DOCTYPE html>
<html lang="en">
<head>
<meta charset="utf-8">
<title>Maverno Holdings LLC — Business Card</title>
<link rel="stylesheet" href="https://fonts.googleapis.com/css2?family=Arimo:wght@400;700&family=Russo+One&display=swap">
<style>
  :root {
    --card-black: #000000;
    --foil-gold: #ffcc00;
    --foil-gold-soft: rgba(255, 204, 0, 0.28);
    --foil-glow: rgba(255, 204, 0, 0.45);
    --band-shadow: rgba(255, 204, 0, 0.35);
    --edge-grey: #5a5a5a;
    --ink: #000000;
  }
  html, body {
    margin: 0;
    padding: 0;
    width: 1200px;
    height: 777px;
    overflow: hidden;
    background: var(--card-black);
  }
  .card {
    position: relative;
    width: 1200px;
    height: 777px;
    background: var(--card-black);
    font-family: "Arimo", Arial, sans-serif;
    color: var(--foil-gold);
  }
  .skyline-art {
    position: absolute;
    left: 365px;
    top: 60px;
    width: 472px;
    height: 412px;
    border-radius: 6px;
    background: linear-gradient(to top,
      var(--foil-gold) 0%,
      var(--foil-gold) 35%,
      var(--foil-gold-soft) 100%);
    box-shadow: 0 0 28px var(--foil-glow);
  }
  .company-name {
    position: absolute;
    left: 0;
    top: 476px;
    width: 1200px;
    margin: 0;
    text-align: center;
    font-family: "Russo One", "Arial Black", sans-serif;
    font-weight: 400;
    font-size: 39px;
    line-height: 48px;
    letter-spacing: 2px;
    color: var(--foil-gold);
  }
  .contact {
    position: absolute;
    top: 536px;
    margin: 0;
    font-size: 29px;
    line-height: 39px;
    font-style: normal;
  }
  .contact-left { left: 80px; text-align: left; }
  .contact-right { right: 97px; text-align: right; }
  .services-band {
    position: absolute;
    left: 0;
    top: 678px;
    width: 1112px;
    height: 40px;
    background: var(--foil-gold);
    box-shadow: 8px 4px 8px var(--band-shadow);
  }
  .services {
    position: absolute;
    left: 77px;
    top: 0;
    margin: 0;
    line-height: 40px;
    font-weight: 700;
    font-size: 33px;
    letter-spacing: 0.2px;
    color: var(--ink);
    white-space: nowrap;
  }
  .card-edge {
    position: absolute;
    left: 0;
    bottom: 6px;
    width: 1200px;
    height: 1px;
    background: var(--edge-grey);
  }
</style>
</head>
<body>
  <main class="card">
    <div class="skyline-art" role="img" aria-label="Glowing gold city skyline of towers and apartment buildings"></div>
    <h1 class="company-name">Maverno Holdings LLC</h1>

    <address class="contact contact-left">
      phone 917-555-2817<br>
      fax 877-555-4139<br>
      Dalen.Okorafor@vintramail.com
    </address>

    <address class="contact contact-right">
      47 Pelbrook Terrace<br>
      North 3D<br>
      Bronx, NY 10482
    </address>

    <div class="services-band">
      <p class="services">General Construction Real Estate Investments and Development</p>
    </div>

    <div class="card-edge"></div>
  </main>
</body>
</html>
```